Agarwood Oud Label Design

I need a circular product label designed for an Agarwood or Bakhoor product. I will provide a rich color scheme picture, as well as the company logo. It may be easier to play with different angles of the logo. So, they are attached also. Label should be 56mm diameter circle label.

```html
<!DOCTYPE html>
<html lang="en">
<head>
<meta charset="utf-8">
<title>Agarwood Label</title>
<link rel="stylesheet" href="https://fonts.googleapis.com/css2?family=Great+Vibes&display=swap">
<style>
  :root {
    --paper: #ffffff;
    --wine-deep: #3a0a0c;
    --wine: #6e1518;
    --wine-bright: #8f1b1f;
    --wood: #9a6a45;
    --wood-light: #c79b6e;
    --silver: #b9b3ab;
    --gold: #d8b24c;
    --gold-dark: #a9822c;
    --ink-light: #ffffff;
    --cream: #f6efe4;
  }
  * { box-sizing: border-box; margin: 0; padding: 0; }
  html, body {
    width: 1200px;
    height: 1200px;
    overflow: hidden;
    background: var(--paper);
  }
  .canvas {
    position: relative;
    width: 1200px;
    height: 1200px;
  }
  .label {
    position: absolute;
    left: 174px;
    top: 174px;
    width: 852px;
    height: 852px;
    border-radius: 50%;
    box-shadow: 0 0 30px 10px rgba(0, 0, 0, 0.55);
    overflow: hidden;
  }
  .label-scene {
    position: absolute;
    inset: 0;
    background:
      radial-gradient(ellipse 30% 22% at 30% 20%, rgba(215, 208, 198, 0.55), transparent 70%),
      radial-gradient(ellipse 28% 22% at 65% 45%, rgba(140, 124, 104, 0.55), transparent 70%),
      radial-gradient(ellipse 20% 24% at 85% 72%, rgba(150, 130, 105, 0.5), transparent 70%),
      radial-gradient(ellipse 45% 20% at 32% 72%, rgba(199, 155, 110, 0.55), transparent 70%),
      radial-gradient(ellipse 80% 70% at 50% 40%, var(--wine-bright), var(--wine) 55%, var(--wine-deep));
  }
  .product-name {
    position: absolute;
    left: 0;
    right: 0;
    top: 337px;
    padding-right: 48px;
    text-align: center;
    font-family: "Great Vibes", cursive;
    font-size: 215px;
    line-height: 1;
    color: var(--ink-light);
    white-space: nowrap;
    text-shadow: 0 2px 6px rgba(0, 0, 0, 0.45);
  }
  .brand-badge {
    position: absolute;
    left: 314px;
    top: 778px;
    width: 574px;
    height: 260px;
    border-radius: 50%;
    background: linear-gradient(180deg, var(--gold), var(--gold-dark));
    padding: 11px;
    box-shadow: 0 4px 10px rgba(0, 0, 0, 0.35);
  }
  .brand-badge-inner {
    width: 100%;
    height: 100%;
    border-radius: 50%;
    background: radial-gradient(ellipse at 50% 40%, var(--wine-bright), var(--wine) 80%);
    display: flex;
    align-items: center;
    justify-content: center;
  }
  .brand-name {
    font-family: "Great Vibes", cursive;
    font-size: 96px;
    line-height: 1;
    color: var(--cream);
    white-space: nowrap;
  }
</style>
</head>
<body>
  <div class="canvas">
    <div class="label">
      <div class="label-scene" role="img" aria-label="Photograph of smoking silver incense burners and agarwood chips on a deep red cloth"></div>
      <div class="product-name">Agarwood</div>
    </div>
    <div class="brand-badge">
      <div class="brand-badge-inner">
        <span class="brand-name">Resin &amp; Rose</span>
      </div>
    </div>
  </div>
</body>
</html>
```